Via Lumo K

Need business cards designed. Project is an Arts Center in Hollywood. It'll include 3 live theatre, a restaurant and event space.

Target Market(s)

Across the board, young and old.

Industry/Entity Type

Entertainment

Contact Information for Business Card

Be creative. This is a creative venture that I'm building.

```html
<!DOCTYPE html>
<html lang="en">
<head>
<meta charset="utf-8">
<title>Via Lumo K – Business Card</title>
<link rel="stylesheet" href="https://fonts.googleapis.com/css2?family=Saira:wght@700&family=Economica:wght@700&family=Open+Sans:wght@300&display=swap">
<style>
  :root {
    --paper: #ffffff;
    --edge: #c9d1d7;
    --band: #638ea3;
    --band-deep: #3d6e87;
    --brand: #3f7088;
    --name: #843a3c;
    --contact-text: #ffffff;
    --icon: #3d6e87;
  }
  html, body {
    margin: 0;
    padding: 0;
    width: 1200px;
    height: 737px;
    overflow: hidden;
    background: var(--paper);
  }
  .card {
    position: relative;
    width: 1200px;
    height: 737px;
    box-sizing: border-box;
    border: 1px solid var(--edge);
    background: var(--paper);
    overflow: hidden;
  }
  .card__shapes {
    position: absolute;
    inset: 0;
    width: 1200px;
    height: 737px;
  }
  .brand-name {
    position: absolute;
    left: 112px;
    top: 80px;
    margin: 0;
    font-family: "Saira", sans-serif;
    font-weight: 700;
    font-size: 76px;
    line-height: 1;
    letter-spacing: -1px;
    color: var(--brand);
  }
  .person-name {
    position: absolute;
    right: 66px;
    top: 252px;
    margin: 0;
    font-family: "Economica", sans-serif;
    font-weight: 700;
    font-size: 84px;
    line-height: 1;
    letter-spacing: 2px;
    color: var(--name);
  }
  .contact {
    position: absolute;
    right: 127px;
    top: 0;
    margin: 0;
    font-family: "Open Sans", sans-serif;
    font-weight: 300;
    font-size: 31px;
    line-height: 45px;
    color: var(--contact-text);
    text-align: right;
    white-space: nowrap;
    font-style: normal;
  }
  .contact--address { top: 418px; }
  .contact--email   { top: 521px; }
  .contact--web     { top: 580px; }
  .contact--phone   { top: 640px; }
  .contact-icon {
    position: absolute;
    width: 40px;
    height: 40px;
  }
  .contact-icon--pin   { left: 1090px; top: 426px; }
  .contact-icon--mail  { left: 1090px; top: 525px; }
  .contact-icon--web   { left: 1090px; top: 580px; }
  .contact-icon--phone { left: 1090px; top: 646px; }
</style>
</head>
<body>
<main class="card">
  <svg class="card__shapes" viewBox="0 0 1200 737" aria-hidden="true">
    <polygon class="band band--top" points="723,0 1200,0 1200,207 673,207" fill="var(--band)"/>
    <polygon class="band-fold" points="541,374 628,374 613,432" fill="var(--band-deep)"/>
    <polygon class="band band--bottom" points="628,374 1200,374 1200,737 533,737" fill="var(--band)"/>
  </svg>

  <h1 class="brand-name">Via Lumo “K”</h1>
  <h2 class="person-name">Person Name</h2>

  <address class="contact contact--address">House No.123, Street Name,<br>City, Country- (code) 123456</address>
  <p class="contact contact--email">E-mail: person’s mail id</p>
  <p class="contact contact--web">Website: compny.com</p>
  <p class="contact contact--phone">Ph.: 000- 00- 12345678</p>

  <svg class="contact-icon contact-icon--pin" viewBox="0 0 40 40" aria-hidden="true">
    <path d="M20 3a11 11 0 0 0-11 11c0 8 11 23 11 23s11-15 11-23A11 11 0 0 0 20 3zm0 15a4 4 0 1 1 0-8 4 4 0 0 1 0 8z" fill="var(--icon)"/>
  </svg>
  <svg class="contact-icon contact-icon--mail" viewBox="0 0 40 40" aria-hidden="true">
    <rect x="3" y="9" width="34" height="23" fill="var(--icon)"/>
    <path d="M4 10l16 13 16-13M4 31l12-11M36 31L24 20" fill="none" stroke="var(--band)" stroke-width="2"/>
  </svg>
  <svg class="contact-icon contact-icon--web" viewBox="0 0 40 40" aria-hidden="true">
    <g fill="none" stroke="var(--icon)" stroke-width="2.4">
      <circle cx="20" cy="20" r="15"/>
      <ellipse cx="20" cy="20" rx="6.5" ry="15"/>
      <line x1="5" y1="20" x2="35" y2="20"/>
      <path d="M8 12h24M8 28h24"/>
    </g>
  </svg>
  <svg class="contact-icon contact-icon--phone" viewBox="0 0 40 40" aria-hidden="true">
    <path d="M11 4l6 8-4 4c2 5 6 9 10 11l4-4 8 6-4 7C18 35 5 22 5 9z" fill="var(--icon)"/>
  </svg>
</main>
</body>
</html>
```